Zorvath GmbH banner ad

Banner ad for Facebook Our company name (logo) Title: Transporter and bus rental Text: Without deposit, super prices

Target Market(s)

Rental

Requirements
Must have
• LOGO from us, Evt. A pair of transporters in the picture

```html
<!DOCTYPE html>
<html lang="de">
<head>
<meta charset="utf-8">
<title>Zorvath GmbH – Transporter and Bus Rental</title>
<link rel="stylesheet" href="https://fonts.googleapis.com/css2?family=Oswald:wght@700&family=Roboto:wght@400&family=Roboto+Condensed:wght@700&display=swap">
<style>
  :root {
    --navy: #17176b;
    --steel: #8d9bb8;
    --band: #b3b3b3;
    --band-dark: #a2a2a2;
    --ink: #1e1e1e;
    --bg-light: #ffffff;
    --bg-grey: #dcdcdc;
    --road-line: rgba(255, 255, 255, 0.85);
    --vehicle-light: #eceff1;
    --vehicle-mid: #b9c0c6;
    --vehicle-dark: #3d4a55;
  }
  * { margin: 0; padding: 0; box-sizing: border-box; }
  html, body { width: 1200px; height: 444px; overflow: hidden; }
  body { background: var(--bg-light); }
  .banner {
    position: relative;
    width: 1200px;
    height: 444px;
    overflow: hidden;
    background:
      radial-gradient(ellipse 55% 70% at 30% 40%, var(--bg-light) 40%, transparent 75%),
      linear-gradient(160deg, var(--bg-light) 30%, var(--bg-grey) 100%);
  }
  .road { position: absolute; inset: 0; }
  .rental-band {
    position: absolute;
    left: 423px;
    top: 329px;
    width: 777px;
    height: 48px;
    background: linear-gradient(90deg, var(--band-dark), var(--band) 40%, var(--band));
  }
  .band-text {
    position: absolute;
    top: 0;
    height: 48px;
    line-height: 48px;
    font-family: "Roboto Condensed", "Arial Narrow", sans-serif;
    font-weight: 700;
    font-size: 30px;
    color: var(--ink);
  }
  .band-text.deposit { left: 219px; }
  .band-text.divider { left: 488px; }
  .band-text.prices { left: 520px; }
  .coach-visual {
    position: absolute;
    left: 22px;
    top: 50px;
    width: 515px;
    height: 360px;
    border-radius: 60px 40px 30px 30px;
    background: linear-gradient(180deg, var(--vehicle-dark) 0%, var(--vehicle-mid) 38%, var(--vehicle-light) 60%, var(--vehicle-mid) 100%);
  }
  .brand {
    position: absolute;
    left: 748px;
    top: 42px;
    display: flex;
    align-items: center;
    gap: 12px;
  }
  .brand-mark { width: 44px; height: 44px; background: var(--navy); }
  .brand-name {
    font-family: "Roboto Condensed", "Arial Narrow", sans-serif;
    font-weight: 700;
    font-size: 34px;
    color: var(--navy);
  }
  .headline {
    position: absolute;
    left: 620px;
    top: 140px;
    width: 540px;
    text-align: center;
  }
  .headline-main {
    display: block;
    font-family: "Oswald", "Arial Narrow", sans-serif;
    font-weight: 700;
    font-size: 94px;
    line-height: 100px;
    color: var(--navy);
    letter-spacing: 1px;
  }
  .headline-sub {
    display: block;
    font-family: "Roboto", Arial, sans-serif;
    font-weight: 400;
    font-size: 51px;
    line-height: 52px;
    color: var(--steel);
    letter-spacing: 0.5px;
  }
</style>
</head>
<body>
  <div class="banner">
    <svg class="road" width="1200" height="444" viewBox="0 0 1200 444" aria-hidden="true">
      <path d="M1060 300 L1200 430" stroke="var(--road-line)" stroke-width="6" fill="none"/>
      <path d="M1120 300 L1180 444" stroke="var(--road-line)" stroke-width="4" fill="none"/>
      <path d="M640 444 L900 300" stroke="var(--road-line)" stroke-width="4" fill="none"/>
    </svg>

    <div class="rental-band">
      <span class="band-text deposit">Ohne Kaution</span>
      <span class="band-text divider">|</span>
      <span class="band-text prices">Superpreise</span>
    </div>

    <div class="coach-visual" role="img" aria-label="White touring coach bus, front three-quarter view"></div>

    <div class="brand">
      <span class="brand-mark"></span>
      <span class="brand-name">Zorvath GmbH</span>
    </div>

    <h1 class="headline">
      <span class="headline-main">TRANSPORTER</span>
      <span class="headline-sub">AND BUS RENTAL</span>
    </h1>
  </div>
</body>
</html>
```